" A Trilo Sistemas é uma empresa que desenvolve sistemas de monitoramento remoto, telemetria via satélite, telecontrole, automaçao, rastreamento de veículos e etc.. Trata-se de uma empresa moderna e jovem, com uma linguagem de comunicaçao moderna e descontraída, sem perder a seriedade. Temos dois segmentos: Corporativo e Varejo. No corporativo, prestamos serviço para grandes empresas como Pedra Alta Minérios por exemplo.Já no varejo atendemos pessoas fisicas ou pequenas empresas. "

```html
<!DOCTYPE html>
<html lang="pt-BR">
<head>
<meta charset="utf-8">
<title>Trilo Sistemas</title>
<link rel="stylesheet" href="https://fonts.googleapis.com/css2?family=Raleway:wght@400;500;600;700;800&display=swap">
<style>
  :root {
    --teal: #3d6f83;
    --teal-dark: #2c5566;
    --teal-deep: #244a59;
    --orange: #e0702e;
    --ink: #2f5f73;
    --white: #ffffff;
    --page-bg: #ffffff;
  }
  * { box-sizing: border-box; margin: 0; padding: 0; }
  html, body { width: 1200px; height: 1200px; overflow: hidden; background: var(--page-bg); }
  body { font-family: "Raleway", sans-serif; position: relative; }

  .site { position: absolute; left: 240px; top: 0; width: 720px; height: 1200px; background: var(--white); overflow: hidden; }

  /* Header */
  .site-header { position: absolute; left: 0; top: 0; width: 720px; height: 53px; }
  .brand { position: absolute; left: 72px; top: 10px; display: flex; align-items: center; gap: 8px; color: var(--teal); font-weight: 700; font-size: 30px; letter-spacing: -0.5px; }
  .brand-dot { width: 26px; height: 26px; border-radius: 50%; background: var(--orange); }
  .main-nav { position: absolute; right: 24px; top: 16px; display: flex; gap: 18px; font-size: 15px; font-weight: 600; color: var(--teal); }
  .main-nav .active { color: var(--teal-deep); font-weight: 800; }

  /* Hero */
  .hero { position: absolute; left: 0; top: 53px; width: 720px; height: 290px; }
  .hero-photo { position: absolute; inset: 0; background: linear-gradient(180deg, #6f8795 0%, #4f6878 45%, #8a9aa3 80%, #b9c2c6 100%); }
  .hero-title { position: absolute; top: 95px; width: 100%; text-align: center; color: var(--white); font-weight: 700; font-size: 22px; }
  .hero-sub { position: absolute; top: 122px; width: 100%; text-align: center; color: var(--white); font-size: 15px; }
  .hero-cta { position: absolute; top: 146px; left: 270px; width: 160px; height: 30px; background: var(--orange); color: var(--white); font-size: 11px; font-weight: 700; letter-spacing: 1px; display: flex; align-items: center; justify-content: center; gap: 8px; border-radius: 2px; }
  .hero-arrow { position: absolute; top: 98px; color: var(--white); font-size: 26px; font-weight: 700; }
  .hero-arrow.prev { left: 50px; }
  .hero-arrow.next { right: 50px; }
  .hero-dots { position: absolute; top: 224px; left: 0; width: 100%; display: flex; justify-content: center; gap: 5px; }
  .hero-dots span { width: 11px; height: 11px; border-radius: 50%; border: 2px solid var(--white); }
  .hero-dots span.on { background: var(--white); }
  .hero-curve { position: absolute; left: 0; top: 230px; }

  /* Intro */
  .intro-graphic { position: absolute; left: 0; top: 312px; }
  .intro-text { position: absolute; left: 20px; top: 488px; width: 320px; text-align: center; color: var(--ink); }
  .intro-title { font-size: 32px; font-weight: 800; letter-spacing: -0.5px; }
  .intro-lead { font-size: 19px; margin-top: 4px; line-height: 1.35; }
  .intro-lead strong { text-decoration: underline; font-weight: 700; }
  .hex-label { position: absolute; color: var(--white); font-weight: 800; font-size: 12px; letter-spacing: 0.5px; }
  .hex-button { position: absolute; border: 2px solid var(--white); border-radius: 4px; color: var(--white); font-size: 10px; padding: 5px 10px; font-weight: 600; }

  /* Showcase */
  .showcase { position: absolute; left: 0; top: 660px; }
  .showcase-text { position: absolute; left: 0; top: 728px; width: 720px; text-align: center; color: var(--white); }
  .showcase-title { font-size: 34px; font-weight: 800; }
  .showcase-lead { font-size: 21px; line-height: 1.45; margin-top: 4px; }
  .showcase-lead strong { text-decoration: underline; font-weight: 700; }
  .device-visual { position: absolute; left: 163px; top: 840px; width: 370px; height: 272px; background: linear-gradient(135deg, #9fb0bc 0%, #4f6f84 45%, #2f4b5c 100%); }
  .showcase-cta { position: absolute; left: 276px; top: 1140px; width: 156px; height: 40px; border: 2px solid var(--white); border-radius: 6px; color: var(--white); font-weight: 700; font-size: 14px; display: flex; align-items: center; justify-content: center; letter-spacing: 0.5px; }
</style>
</head>
<body>
<div class="site">

  <header class="site-header">
    <div class="brand"><span class="brand-dot"></span>trilo</div>
    <nav class="main-nav">
      <span class="active">HOME</span>
      <span>Tecnologia</span>
      <span>Segmentos</span>
      <span>Serviços</span>
      <span>Trilo Web</span>
    </nav>
  </header>

  <section class="hero">
    <div class="hero-photo" role="img" aria-label="Fotografia de avião, porto com contêineres, caminhão e mapa-múndi em tons de azul acinzentado"></div>
    <p class="hero-title">só a trilo tem a tecnologia que move o mundo</p>
    <p class="hero-sub">somos apaixonados por monitoramento &amp; Segurança</p>
    <div class="hero-cta">O QUE FAZEMOS
      <svg width="12" height="8" viewBox="0 0 12 8"><path d="M1 1 L6 6 L11 1" fill="none" stroke="#fff" stroke-width="2"/></svg>
    </div>
    <span class="hero-arrow prev">‹</span>
    <span class="hero-arrow next">›</span>
    <div class="hero-dots"><span></span><span class="on"></span><span></span><span></span></div>
    <svg class="hero-curve" width="720" height="70" viewBox="0 0 720 70">
      <path d="M0 22 Q360 95 720 22 L720 70 L0 70 Z" fill="var(--orange)"/>
      <path d="M0 34 Q360 100 720 34 L720 70 L0 70 Z" fill="var(--white)"/>
    </svg>
  </section>

  <svg class="intro-graphic" width="720" height="372" viewBox="0 0 720 372">
    <defs>
      <linearGradient id="hexEmpresa" x1="0" y1="0" x2="1" y2="1"><stop offset="0" stop-color="#5a7588"/><stop offset="1" stop-color="#2c4251"/></linearGradient>
      <linearGradient id="hexConsultoria" x1="0" y1="0" x2="1" y2="1"><stop offset="0" stop-color="#e9eef1"/><stop offset="1" stop-color="#a9b8c2"/></linearGradient>
      <linearGradient id="hexTecnologia" x1="0" y1="0" x2="1" y2="1"><stop offset="0" stop-color="#4aa3d8"/><stop offset="1" stop-color="#1d5f95"/></linearGradient>
      <linearGradient id="hexSolucoes" x1="0" y1="0" x2="0" y2="1"><stop offset="0" stop-color="#9db9cc"/><stop offset="0.5" stop-color="#7a8a52"/><stop offset="1" stop-color="#8a6a3a"/></linearGradient>
    </defs>
    <g role="img" aria-label="Foto de escritório da empresa">
      <polygon points="434,96 391,22 305,22 262,96 305,170 391,170" fill="url(#hexEmpresa)" stroke="var(--teal)" stroke-width="9"/>
    </g>
    <g role="img" aria-label="Foto de documentos e gráficos de consultoria">
      <polygon points="592,84 551,13 467,13 426,84 467,155 551,155" fill="url(#hexConsultoria)" stroke="var(--orange)" stroke-width="9"/>
    </g>
    <g role="img" aria-label="Foto de profissional usando tela digital">
      <polygon points="516,252 474,180 390,180 348,252 390,324 474,324" fill="url(#hexTecnologia)" stroke="var(--teal)" stroke-width="9"/>
    </g>
    <g role="img" aria-label="Foto de plantação e campo ao pôr do sol">
      <polygon points="684,228 642,156 558,156 516,228 558,300 642,300" fill="url(#hexSolucoes)" stroke="var(--orange)" stroke-width="9"/>
    </g>
    <path d="M0 332 Q360 270 720 332 L720 372 L0 372 Z" fill="var(--orange)"/>
  </svg>
  <span class="hex-label" style="left:317px;top:392px;">A EMPRESA</span>
  <span class="hex-button" style="left:318px;top:412px;">SAIBA MAIS</span>
  <span class="hex-label" style="left:474px;top:408px;color:#2c4251;background:rgba(255,255,255,.6);padding:1px 4px;">CONSULTORIA</span>
  <span class="hex-label" style="left:370px;top:570px;">TECNOLOGIA</span>
  <span class="hex-label" style="left:560px;top:562px;">SOLUÇÕES</span>
  <div class="intro-text">
    <p class="intro-title">A TRILO MUDOU !</p>
    <p class="intro-lead">Estamos sempre trabalhando<br>para <strong>melhorar pra você</strong> !</p>
  </div>

  <svg class="showcase" width="720" height="540" viewBox="0 0 720 540">
    <path d="M0 50 Q360 -4 720 50 L720 540 L0 540 Z" fill="var(--teal)"/>
    <rect x="0" y="300" width="720" height="240" fill="var(--teal-dark)" opacity="0.35"/>
  </svg>
  <div class="showcase-text">
    <p class="showcase-title">LOREM IPSUM DOLOR</p>
    <p class="showcase-lead">Estamos sempre trabalhando<br>para <strong>melhorar pra você</strong> !</p>
  </div>
  <div class="device-visual" role="img" aria-label="Ilustração de monitor, tablet e celular exibindo a plataforma de monitoramento"></div>
  <div class="showcase-cta">SAIBA MAIS</div>

</div>
</body>
</html>
```